" Venda de planos de assistência familiar oferecendo uma rede descontos e funerais para os seus associados ; Serviços funerários; Venda de coroa de flores e arranjos. "

```html
<!DOCTYPE html>
<html lang="pt-BR">
<head>
<meta charset="UTF-8">
<title>Parque Jardim Sereno — Cartão de visita</title>
<link href="https://fonts.googleapis.com/css2?family=Montserrat:wght@400;600;800&display=swap" rel="stylesheet">
<style>
  :root {
    --teal: #1a8a7e;
    --teal-dark: #0f6e64;
    --paper: #ffffff;
    --paper-shade: #f1f3f3;
    --ink: #4a4f52;
    --stage: #e4e6e7;
  }
  * { box-sizing: border-box; margin: 0; padding: 0; }
  html, body { width: 1200px; height: 1200px; overflow: hidden; }
  body {
    background: var(--stage);
    font-family: "Montserrat", sans-serif;
    position: relative;
  }
  .card {
    position: absolute;
    background: var(--paper);
    border-radius: 18px;
    overflow: hidden;
    box-shadow: 0 6px 24px rgba(0,0,0,0.12);
  }
  /* Front */
  .card-front {
    left: 90px; top: 250px; width: 400px; height: 700px;
    background: linear-gradient(180deg, var(--paper) 0%, var(--paper-shade) 100%);
  }
  .front-brand {
    position: absolute; left: 0; right: 0; top: 250px;
    display: flex; flex-direction: column; align-items: center; gap: 22px;
  }
  .brand-dot {
    width: 120px; height: 120px; border-radius: 50%;
    background: var(--teal);
  }
  .brand-name {
    color: var(--teal);
    font-weight: 800;
    font-size: 28px;
    letter-spacing: 1px;
    text-transform: uppercase;
    text-align: center;
    line-height: 1.2;
  }
  .front-band {
    position: absolute; left: 0; right: 0; bottom: 0; height: 110px;
    background: var(--teal);
  }
  .front-band-line {
    position: absolute; left: 0; right: 0; bottom: 70px; height: 6px;
    background: var(--paper);
  }
  /* Back */
  .card-back {
    left: 530px; top: 423px; width: 620px; height: 354px;
  }
  .back-circle {
    position: absolute; left: -60px; top: -110px;
    width: 340px; height: 340px; border-radius: 50%;
    background: var(--teal);
  }
  .back-info {
    position: absolute; left: 300px; top: 60px; right: 30px;
    color: var(--ink);
  }
  .person-name { font-size: 20px; font-weight: 600; }
  .person-role { font-size: 14px; font-weight: 400; margin-bottom: 22px; }
  .contact-list { list-style: none; display: flex; flex-direction: column; gap: 10px; }
  .contact-item { display: flex; align-items: flex-start; gap: 10px; font-size: 12px; line-height: 1.35; }
  .contact-icon { flex: 0 0 20px; width: 20px; height: 20px; }
  .back-band {
    position: absolute; left: 0; right: 0; bottom: 0; height: 34px;
    background: var(--teal);
  }
  .back-band-line {
    position: absolute; left: 0; right: 0; bottom: 20px; height: 4px;
    background: var(--paper);
  }
</style>
</head>
<body>
  <section class="card card-front">
    <div class="front-brand">
      <span class="brand-dot"></span>
      <span class="brand-name">Parque<br>Jardim Sereno</span>
    </div>
    <div class="front-band"></div>
    <div class="front-band-line"></div>
  </section>

  <section class="card card-back">
    <div class="back-circle"></div>
    <div class="back-info">
      <p class="person-name">Nome Completo</p>
      <p class="person-role">Cargo</p>
      <ul class="contact-list">
        <li class="contact-item">
          <svg class="contact-icon" viewBox="0 0 20 20"><circle cx="10" cy="10" r="10" fill="#1a8a7e"/><path d="M7 5.5l2 2-1 1.2c.6 1.3 1.6 2.3 2.9 2.9l1.2-1 2 2-1.3 1.4c-3.4-.4-6.7-3.7-7.1-7.1z" fill="#fff"/></svg>
          <span>(00) 0000-0000</span>
        </li>
        <li class="contact-item">
          <svg class="contact-icon" viewBox="0 0 20 20"><circle cx="10" cy="10" r="10" fill="#1a8a7e"/><path d="M10 4.5a3.5 3.5 0 0 1 3.5 3.5c0 2.6-3.5 7-3.5 7s-3.5-4.4-3.5-7A3.5 3.5 0 0 1 10 4.5z" fill="#fff"/><circle cx="10" cy="8" r="1.3" fill="#1a8a7e"/></svg>
          <span>Seu endereço - Bairro<br>Cidade - Estado<br>CEP 0000-0000</span>
        </li>
        <li class="contact-item">
          <svg class="contact-icon" viewBox="0 0 20 20"><circle cx="10" cy="10" r="10" fill="#1a8a7e"/><circle cx="10" cy="10" r="5" fill="none" stroke="#fff" stroke-width="1.3"/><path d="M5 10h10M10 5c-2 3-2 7 0 10M10 5c2 3 2 7 0 10" fill="none" stroke="#fff" stroke-width="1"/></svg>
          <span>www.jardimsereno.com.br</span>
        </li>
        <li class="contact-item">
          <svg class="contact-icon" viewBox="0 0 20 20"><circle cx="10" cy="10" r="10" fill="#1a8a7e"/><rect x="5" y="6.5" width="10" height="7" fill="none" stroke="#fff" stroke-width="1.3"/><path d="M5 6.5l5 4 5-4" fill="none" stroke="#fff" stroke-width="1.3"/></svg>
          <span>contato@jardimsereno.com.br</span>
        </li>
      </ul>
    </div>
    <div class="back-band"></div>
    <div class="back-band-line"></div>
  </section>
</body>
</html>
```